Personal Vistrano Banner

I am creating a personal brand for myself. I want a vistrano banner that inspires and motivates people to reach their epic awesomeness. I am creating and designing my personal brand. It can be a background with words on a scenery a picture or 3d graphic. If someone looked at it, they should say it is aggressively epic and motivating. It should be dramatic and bold.
My personal goal is to help as many people reach financial freedom as possible, and challenge and break their own limiting beliefs. This personal brand will be integrated into my zomblat, quorVex, and professional vistrano fanpage (in addition to personal page). My goals are to open up a school for the underpriveleged children, develop my network marketing company team, and become a billionaire in the process. I want to attract people to me that really identify with doing what most think is impossible in terms of personal growth, impact to the world and financial wealth.
Updates

I have updated my brief with more background, and added a new comment to the discussion section to give you more to work with.

Reason: To give designers more time and to create a second and third place prize.

Reason: I am giving designers time to submit more designs

Target Market(s)

business professionals, and people with an entrepreneurial spirit.

Industry/Entity Type

Financial

Requirements
Must have
• It must be the exact dimensions required for vistrano banners. It should not be bigger or smaller. exact!!!

```html
<!DOCTYPE html>
<html lang="en">
<head>
<meta charset="utf-8">
<title>Release Your Epic – Vistrano Banner Concepts</title>
<link rel="stylesheet" href="https://fonts.googleapis.com/css2?family=Bebas+Neue&family=Oswald:wght@500&display=swap">
<style>
  :root {
    --page-bg: #ffffff;
    --number-grey: #a8a8a8;
    --epic-yellow: #fff200;
    --release-cyan: #12b4ec;
    --ember-orange: #d9661c;
    --night: #050508;
    --magenta-glow: #5a1048;
    --indigo-glow: #2a1a7a;
    --ice-blue: #2c8fd6;
    --mane-grey: #6d6d6d;
  }
  * { margin: 0; padding: 0; box-sizing: border-box; }
  html, body {
    width: 1200px;
    height: 1000px;
    overflow: hidden;
    background: var(--page-bg);
  }
  .concept-sheet {
    position: relative;
    width: 1200px;
    height: 1000px;
  }
  .concept-number {
    position: absolute;
    left: 112px;
    font-family: "Oswald", sans-serif;
    font-weight: 500;
    font-size: 40px;
    line-height: 1;
    color: var(--number-grey);
  }
  .banner {
    position: absolute;
    left: 217px;
    width: 766px;
    height: 305px;
    display: block;
  }
  .banner-one { top: 20px; }
  .banner-two { top: 347px; }
  .banner-three { top: 674px; }
  .epic-word {
    font-family: "Bebas Neue", sans-serif;
    fill: var(--epic-yellow);
  }
  .release-line {
    font-family: "Bebas Neue", sans-serif;
    fill: var(--release-cyan);
  }
</style>
</head>
<body>
<main class="concept-sheet">

  <span class="concept-number" style="top:188px">1.</span>
  <span class="concept-number" style="top:508px">2.</span>
  <span class="concept-number" style="top:826px">3.</span>

  <!-- Concept one: twin lions in warm and cool light -->
  <svg class="banner banner-one" viewBox="0 0 766 305" xmlns="http://www.w3.org/2000/svg">
    <defs>
      <linearGradient id="warmCoolSplit" x1="0" x2="1" y1="0" y2="0">
        <stop offset="0" stop-color="var(--ember-orange)"/>
        <stop offset="0.22" stop-color="#7a3a1e"/>
        <stop offset="0.38" stop-color="var(--magenta-glow)"/>
        <stop offset="0.5" stop-color="var(--night)"/>
        <stop offset="0.62" stop-color="var(--indigo-glow)"/>
        <stop offset="0.8" stop-color="#1f4f86"/>
        <stop offset="1" stop-color="var(--ice-blue)"/>
      </linearGradient>
      <mask id="epicGapOne">
        <rect width="766" height="305" fill="#fff"/>
        <rect x="0" y="143" width="766" height="36" fill="#000"/>
      </mask>
    </defs>
    <rect width="766" height="305" fill="url(#warmCoolSplit)" role="img" aria-label="Two mirrored lion faces, one glowing orange on the left and one glowing blue on the right, over a dark smoky backdrop"/>
    <text class="epic-word" x="220" y="245" font-size="230" textLength="328" lengthAdjust="spacingAndGlyphs" mask="url(#epicGapOne)">EPIC</text>
    <text class="release-line" x="220" y="176" font-size="44" textLength="328" lengthAdjust="spacing">RELEASE YOUR</text>
  </svg>

  <!-- Concept two: mirrored roaring lions on black -->
  <svg class="banner banner-two" viewBox="0 0 766 305" xmlns="http://www.w3.org/2000/svg">
    <defs>
      <radialGradient id="maneGlow" cx="0.5" cy="0.45" r="0.55">
        <stop offset="0" stop-color="var(--mane-grey)"/>
        <stop offset="0.45" stop-color="#2e2e30"/>
        <stop offset="1" stop-color="var(--night)"/>
      </radialGradient>
      <mask id="epicGapTwo">
        <rect width="766" height="305" fill="#fff"/>
        <rect x="0" y="134" width="766" height="38" fill="#000"/>
      </mask>
    </defs>
    <rect width="766" height="305" fill="url(#maneGlow)" role="img" aria-label="Two mirrored roaring lions in grey with a red and cyan split effect on a black background"/>
    <text class="epic-word" x="220" y="238" font-size="230" textLength="328" lengthAdjust="spacingAndGlyphs" mask="url(#epicGapTwo)">EPIC</text>
    <text class="release-line" x="220" y="170" font-size="44" textLength="328" lengthAdjust="spacing">RELEASE YOUR</text>
  </svg>

  <!-- Concept three: roaring lion between fire and ice -->
  <svg class="banner banner-three" viewBox="0 0 766 305" xmlns="http://www.w3.org/2000/svg">
    <defs>
      <linearGradient id="fireIce" x1="0" x2="1" y1="0" y2="0">
        <stop offset="0" stop-color="#c2541a"/>
        <stop offset="0.15" stop-color="#f0a25a"/>
        <stop offset="0.32" stop-color="#e8dcd2"/>
        <stop offset="0.5" stop-color="#8a8a8a"/>
        <stop offset="0.68" stop-color="#dce8f0"/>
        <stop offset="0.85" stop-color="#5bb6e8"/>
        <stop offset="1" stop-color="#1470b8"/>
      </linearGradient>
      <mask id="epicGapThree">
        <rect width="766" height="305" fill="#fff"/>
        <rect x="0" y="203" width="766" height="38" fill="#000"/>
      </mask>
    </defs>
    <rect width="766" height="305" fill="url(#fireIce)" role="img" aria-label="A roaring black and white lion at centre, with an orange fire burst on the left and a blue ice burst on the right"/>
    <text class="epic-word" x="220" y="292" font-size="230" textLength="328" lengthAdjust="spacingAndGlyphs" mask="url(#epicGapThree)">EPIC</text>
    <text class="release-line" x="220" y="238" font-size="44" textLength="328" lengthAdjust="spacing">RELEASE YOUR</text>
  </svg>

</main>
</body>
</html>
```